Classy Home Bar menu in word format

The name of the bar is Bar Penhallow
8x10 bar menu black/gold lettering
classy coloring/font. Cover page for who we are. Next 9 pages will be drinks
drinks need to have a spot for names - brief description and a box for a picture
Drink menu should have a speakeasy vibe and be at least 10 pages long with different layouts

Target Market(s)

Visitors to our home. Friends family and guests

Industry/Entity Type

Bar guests

Font styles to use
Script

Requirements
Must have
• Class, easily editable, spots for pictures

```html
<!DOCTYPE html>
<html lang="en">
<head>
<meta charset="utf-8">
<title>Bar Penhallow – Menu</title>
<link rel="stylesheet" href="https://fonts.googleapis.com/css2?family=Pinyon+Script&family=Montserrat:wght@400;600&display=swap">
<style>
  :root {
    --backdrop: #b3b4b3;
    --page: #2b2b2b;
    --page-tone: #363636;
    --accent: #ef8b22;
    --ink-dark: #2b2b2b;
    --ink-light: #ffffff;
  }
  * { margin: 0; padding: 0; box-sizing: border-box; }
  html, body { width: 1200px; height: 761px; overflow: hidden; background: var(--backdrop); }
  .canvas { position: relative; width: 1200px; height: 761px; font-family: "Montserrat", sans-serif; }
  .page { position: absolute; top: 30px; width: 561px; height: 701px;
    background: radial-gradient(circle at 50% 45%, var(--page-tone), var(--page) 70%); }
  .page--cover { left: 29px; }
  .page--drinks { left: 610px; }
  .frame { position: absolute; left: 34px; top: 35px; width: 492px; height: 631px; border: 2px solid var(--accent); }

  .bar-name { position: absolute; left: 0; right: 0; top: 62px; text-align: center;
    font-family: "Pinyon Script", cursive; font-size: 62px; color: var(--accent); line-height: 1; }
  .cocktail-art { position: absolute; left: 160px; top: 174px; width: 232px; height: 302px;
    background: radial-gradient(ellipse at 50% 30%, #f5c79a, #e9914a 55%, rgba(43,43,43,0) 75%); }
  .who-heading { position: absolute; left: 0; right: 0; top: 500px; text-align: center;
    font-family: "Pinyon Script", cursive; font-size: 34px; color: var(--ink-light); line-height: 1.2; }
  .who-text { position: absolute; left: 76px; width: 410px; top: 548px; text-align: center;
    color: var(--ink-light); font-size: 9.3px; line-height: 10.9px; }

  .drinks-ribbon { position: absolute; left: 119px; top: 15px; width: 323px; height: 41px; }
  .drinks-title { position: absolute; left: 119px; top: 15px; width: 323px; height: 41px; text-align: center;
    font-family: "Pinyon Script", cursive; font-size: 34px; line-height: 41px; color: var(--ink-dark); font-weight: 600; }

  .drink { position: absolute; width: 253px; }
  .drink-name { position: relative; height: 28px; }
  .drink-name svg { position: absolute; left: 0; top: 0; }
  .drink-name span { position: absolute; left: 9px; top: 0; font-family: "Pinyon Script", cursive;
    font-size: 22px; line-height: 28px; color: var(--ink-dark); font-weight: 600; }
  .drink-desc { margin-top: 17px; width: 240px; color: var(--ink-light); font-size: 9.2px; line-height: 11px; }
  .drink-price { margin-top: 12px; color: var(--ink-light); font-size: 12.5px; font-weight: 600; }
  .drink-rule { margin-top: 7px; width: 234px; height: 1px; background: var(--accent); }
  .drink-photo { position: absolute; width: 137px; height: 102px; border: 1.5px solid var(--accent); border-radius: 8px; }
  .photo--papaya { background: linear-gradient(135deg, #f2efec, #e8573a 55%, #d9d4cf); }
  .photo--smoothie { background: linear-gradient(160deg, #2a201b, #c98e72 55%, #3a2e28); }
  .photo--pineapple { background: linear-gradient(150deg, #f1f1f1, #efe08a 55%, #6f7a4a); }
  .photo--carrot { background: linear-gradient(150deg, #3d7d3a, #f29b24 55%, #2e8fb0); }
</style>
</head>
<body>
<div class="canvas">
  <section class="page page--cover">
    <div class="frame"></div>
    <h1 class="bar-name">Bar Penhallow</h1>
    <div class="cocktail-art" role="img" aria-label="Illustration of a martini glass with an olive on a cocktail pick"></div>
    <h2 class="who-heading">Who We Are</h2>
    <p class="who-text">Lorem ipsum dolor sit amet, consectetuer adipiscing elit, sed diam nonummy nibh euismod tincidunt ut laoreet dolore magna aliquam erat volutpat. Ut wisi enim ad minim veniam, quis nostrud exerci tation ullamcorper suscipit lobortis nisl ut aliquip ex ea commodo consequat. Duis autem vel eum iriure dolor in hendrerit in vulputate velit esse molestie consequat, vel illum dolore eu feugiat nulla facilisis at vero eros et accumsan et iusto odio dignissim qui blandit praesent luptatum zzril delenit augue duis dolore te feugait nulla facilisi. Lorem ipsum dolor sit amet, cons ectetuer adipiscing elit, sed diam nonummy nibh euismod tincidunt ut laoreet dolore magna aliquam erat volutpat. Ut wisi enim ad minim veniam, quis nostrud exerci tation</p>
  </section>

  <section class="page page--drinks">
    <div class="frame"></div>
    <svg class="drinks-ribbon" viewBox="0 0 323 41" aria-hidden="true">
      <polygon points="0,0 323,0 310,20.5 323,41 0,41 13,20.5" fill="var(--accent)"/>
    </svg>
    <h2 class="drinks-title">Drinks</h2>

    <article class="drink" style="left:67px;top:90px">
      <div class="drink-name"><svg width="253" height="28"><polygon points="0,0 228,0 253,28 0,28" fill="var(--accent)"/></svg><span>Lorem ipsum dolor sit amet</span></div>
      <p class="drink-desc">Lorem ipsum dolor sit amet, consectetuer adipiscing elit, sed diam nonummy nibh euismod tincidunt ut laoreet dolore magna aliquam erat volutpat.</p>
      <p class="drink-price">$0.00</p>
      <div class="drink-rule"></div>
    </article>
    <div class="drink-photo photo--papaya" style="left:357px;top:95px" role="img" aria-label="Photo of a red papaya juice with mint and papaya slices"></div>

    <div class="drink-photo photo--smoothie" style="left:67px;top:242px" role="img" aria-label="Photo of fruit smoothies in tall glasses with strawberries"></div>
    <article class="drink" style="left:227px;top:238px">
      <div class="drink-name"><svg width="253" height="28"><polygon points="0,0 228,0 253,28 0,28" fill="var(--accent)"/></svg><span>Lorem ipsum dolor sit amet</span></div>
      <p class="drink-desc">Lorem ipsum dolor sit amet, consectetuer adipiscing elit, sed diam nonummy nibh euismod tincidunt ut laoreet dolore magna aliquam erat volutpat.</p>
      <p class="drink-price">$0.00</p>
      <div class="drink-rule"></div>
    </article>

    <article class="drink" style="left:67px;top:386px">
      <div class="drink-name"><svg width="253" height="28"><polygon points="0,0 228,0 253,28 0,28" fill="var(--accent)"/></svg><span>Lorem ipsum dolor sit amet</span></div>
      <p class="drink-desc">Lorem ipsum dolor sit amet, consectetuer adipiscing elit, sed diam nonummy nibh euismod tincidunt ut laoreet dolore magna aliquam erat volutpat.</p>
      <p class="drink-price">$0.00</p>
      <div class="drink-rule"></div>
    </article>
    <div class="drink-photo photo--pineapple" style="left:357px;top:392px" role="img" aria-label="Photo of pineapple juice in glasses beside a pineapple"></div>

    <div class="drink-photo photo--carrot" style="left:67px;top:534px" role="img" aria-label="Photo of carrot and ginger juice in a glass"></div>
    <article class="drink" style="left:227px;top:530px">
      <div class="drink-name"><svg width="253" height="28"><polygon points="0,0 228,0 253,28 0,28" fill="var(--accent)"/></svg><span>Lorem ipsum dolor sit amet</span></div>
      <p class="drink-desc">Lorem ipsum dolor sit amet, consectetuer adipiscing elit, sed diam nonummy nibh euismod tincidunt ut laoreet dolore magna aliquam erat volutpat.</p>
      <p class="drink-price">$0.00</p>
      <div class="drink-rule"></div>
    </article>
  </section>
</div>
</body>
</html>
```